Stationery Design Project

We need a stationery design for our Norwegian trucking company. We have existed for about 15 years and our 12 drivers uses relatively new vehicles to transport goods around in northern Norway. Long distance routes with fresh fish og food transport is our main operations.

We have already made alogo that's printed on our trucks. The logo and a picture of our trucks is attached. I think the logo i crappy, but since its already in use, changing it is not an option in this round. Still using a better colour scheme in the overall stationery and more interesting fonts is possible (altso in the logo).

Company details:
Name: Vikmarka AS
Organisation nr 983 517 608
Post adress: 8640 Brekka

I like minimalism and simplicity. I am avalibly for questions in normal GMT working hours either here or on mail: kjell@brekkafrakt.no

Reason: Hi. Im extending the deadline because I needed some time to find a vector file of our logo. Sorry for the inconvenience

Hi, and thanks for all your interest in the project. Some updates:

-          I have decided to commit to using one of the designs. Some designer will get the payment.

-          I have extended the deadline with 24 hours since I needed some time to find our firms vector logo (a slow Swedish man was holding me up)

-          We will not choose a design before the deadline. No need to rush.

-          We have received a lot of great design and think there is a need to specified the product we want to make:

o   Business Card for all our employers. I just need the design and will duplicate with the correct numbers and name myself. The information on should be: Logo, employer’s name, Phone number, email, website, Postal number and address. Use this as a template: logo, Leif Dahlberg, 47382950, Leif@brekkafrakt.no,, brekkafrakt.no, 8640 Brekka. The order and placement of the information is your creative decision.

o   Stickers to put on the goods we travel. On the sticker the should be the following information: Logo, phone number, Tekst and link: Fraktæ av Vikmarka. Ke du syns? Brekkafrakt.no/tilbakemelding (this means: Handled by Vikmarka. What do you think Brekkafrakt.no/feedback -à the link will be a feedback form). The placement the information and size is your creative decision with some stings: we have been thinking of using Prentolo for printing and see that a size about 6x6 cm, 8x5 or something like that. (with 3000 copies our budget is 200 punds). Any suggestions of other suppliers are welcome. Prentolo price calculator http://www.prentoloprints.example/digital-litho-printing/printing-labels-tags/stickers/

o   Letterhead with logo, address, phone number and organizational number.

o   Envelopes with logo,address, phone number and organizational number.

Have a nice day.

 

 

• Using the blue colour in the logo and using a similar graphic approch.

```html
<!DOCTYPE html>
<html lang="no">
<head>
<meta charset="utf-8">
<title>Vikmarka AS – Stationery</title>
<link rel="stylesheet" href="https://fonts.googleapis.com/css2?family=Open+Sans:wght@300;400;600;700&display=swap">
<style>
  :root {
    --stage: #a6a6a6;
    --paper: #ffffff;
    --blue-deep: #22479a;
    --blue-mid: #2364a8;
    --blue-light: #2480b0;
    --blue-text: #1d6fb0;
    --ink-soft: #6d6d6d;
  }
  * { box-sizing: border-box; margin: 0; padding: 0; }
  html, body { width: 1200px; height: 900px; overflow: hidden; }
  body {
    position: relative;
    background: var(--stage);
    font-family: "Open Sans", sans-serif;
  }
  .sprites { position: absolute; width: 0; height: 0; }

  .wordmark {
    display: inline-flex;
    align-items: center;
    gap: 0.35em;
    font-weight: 700;
    color: var(--blue-deep);
    letter-spacing: 0.01em;
    line-height: 1;
    white-space: nowrap;
  }
  .wordmark::before {
    content: "";
    width: 0.6em; height: 0.6em;
    border-radius: 50%;
    background: currentColor;
  }
  .wordmark--white { color: #fff; }

  .contact { list-style: none; color: var(--ink-soft); font-weight: 300; }
  .contact li { display: flex; align-items: center; gap: 4px; white-space: nowrap; }
  .contact svg { fill: var(--blue-text); flex: none; }

  .base-band { position: absolute; left: 0; bottom: 0; width: 100%; display: block; }
  .org-number {
    position: absolute; right: 10px; bottom: 5px;
    color: #fff; font-size: 10px; font-weight: 300;
  }

  /* Business card – back */
  .card { position: absolute; width: 251px; height: 143px; border-radius: 8px; overflow: hidden; }
  .card--back {
    left: 139px; top: 46px;
    background: radial-gradient(ellipse at 38% 60%, var(--blue-light) 0%, var(--blue-mid) 45%, var(--blue-deep) 100%);
    display: flex; align-items: center; justify-content: center;
  }
  .card--back .wordmark { font-size: 22px; }

  /* Business card – front */
  .card--front { left: 265px; top: 210px; background: var(--paper); }
  .card--front .wordmark { position: absolute; left: 13px; top: 18px; font-size: 14px; }
  .card__person { position: absolute; left: 33px; top: 82px; }
  .card__name { font-size: 9px; font-weight: 600; color: var(--blue-text); }
  .card__role { font-size: 6px; color: var(--ink-soft); }
  .card--front .contact { position: absolute; left: 159px; top: 77px; font-size: 5.5px; line-height: 9px; }

  /* Letterhead */
  .letterhead {
    position: absolute; left: 551px; top: 64px; width: 613px; height: 793px;
    background: var(--paper); overflow: hidden;
  }
  .letterhead .wordmark { position: absolute; left: 31px; top: 50px; font-size: 34px; }
  .letterhead .contact { position: absolute; left: 481px; top: 61px; font-size: 9.5px; line-height: 12px; }

  /* Envelope */
  .envelope { position: absolute; left: 69px; top: 377px; width: 685px; height: 393px; }
  .envelope__flap { position: absolute; left: 0; top: 0; width: 685px; height: 95px; display: block; }
  .envelope__flap-mark {
    position: absolute; left: 342px; top: 44px;
    transform: translate(-50%, -50%) rotate(180deg);
    font-size: 17px;
  }
  .envelope__body {
    position: absolute; left: 0; top: 95px; width: 685px; height: 298px;
    background: var(--paper); overflow: hidden;
    box-shadow: 0 0 4px rgba(0,0,0,0.25);
  }
  .envelope__body .wordmark { position: absolute; left: 17px; top: 24px; font-size: 27px; }
  .envelope__body .contact { position: absolute; left: 23px; top: 70px; font-size: 9.5px; line-height: 12px; }
</style>
</head>
<body>

<svg class="sprites" aria-hidden="true">
  <defs>
    <symbol id="icon-home" viewBox="0 0 10 10"><path d="M5 1 L9.5 5 H8 V9 H6 V6.5 H4 V9 H2 V5 H0.5 Z"/></symbol>
    <symbol id="icon-phone" viewBox="0 0 10 10"><path d="M1 4 C1 2 9 2 9 4 L7.5 5 L6.5 4 H3.5 L2.5 5 Z M2.5 5.5 H7.5 L8.5 8 H1.5 Z"/></symbol>
    <symbol id="icon-mail" viewBox="0 0 10 10"><path d="M1 2.5 H9 V7.5 H1 Z M1.6 3 L5 5.5 L8.4 3" fill="none" stroke="currentColor" stroke-width="0.9"/></symbol>
    <symbol id="icon-web" viewBox="0 0 10 10"><circle cx="5" cy="5" r="4"/><path d="M1 5 H9 M5 1 V9" stroke="#fff" stroke-width="0.8"/></symbol>
    <linearGradient id="band-blue" x1="0" y1="0" x2="1" y2="0">
      <stop offset="0" stop-color="#2353a0"/><stop offset="0.55" stop-color="#2381b2"/><stop offset="1" stop-color="#22479a"/>
    </linearGradient>
    <linearGradient id="flap-blue" x1="0" y1="1" x2="1" y2="0">
      <stop offset="0" stop-color="#22479a"/><stop offset="0.6" stop-color="#2381b2"/><stop offset="1" stop-color="#2364a8"/>
    </linearGradient>
  </defs>
</svg>

<section class="card card--back" aria-label="Business card, back">
  <span class="wordmark wordmark--white">Vikmarka</span>
</section>

<section class="card card--front" aria-label="Business card, front">
  <span class="wordmark">Vikmarka</span>
  <div class="card__person">
    <p class="card__name">Leif Dahlberg</p>
    <p class="card__role">Marketing Manager</p>
  </div>
  <ul class="contact">
    <li><svg width="7" height="7"><use href="#icon-phone"/></svg>47382950</li>
    <li><svg width="7" height="7" style="color:var(--blue-text)"><use href="#icon-mail"/></svg>Leif@brekkafrakt.no</li>
    <li><svg width="7" height="7"><use href="#icon-web"/></svg>www.brekkafrakt.no</li>
    <li><svg width="7" height="7"><use href="#icon-home"/></svg>8640 Brekka</li>
  </ul>
  <svg class="base-band" viewBox="0 0 251 30" width="251" height="30" preserveAspectRatio="none" aria-hidden="true">
    <path d="M0 22 Q130 28 251 0 V30 H0 Z" fill="url(#band-blue)"/>
  </svg>
</section>

<section class="letterhead" aria-label="Letterhead">
  <span class="wordmark">Vikmarka</span>
  <ul class="contact">
    <li><svg width="8" height="8"><use href="#icon-home"/></svg>8640 Brekka</li>
    <li><svg width="8" height="8"><use href="#icon-phone"/></svg>47382950</li>
  </ul>
  <svg class="base-band" viewBox="0 0 613 80" width="613" height="80" preserveAspectRatio="none" aria-hidden="true">
    <path d="M0 54 Q320 66 613 0 V80 H0 Z" fill="url(#band-blue)"/>
  </svg>
  <p class="org-number">Organisation Number 983 517 608</p>
</section>

<section class="envelope" aria-label="Envelope">
  <svg class="envelope__flap" viewBox="0 0 685 95" aria-hidden="true">
    <path d="M0 95 L24 32 Q29 22 40 21 L342 0 L668 20 Q678 21 682 32 L685 95 Z" fill="url(#flap-blue)"/>
  </svg>
  <span class="wordmark wordmark--white envelope__flap-mark">Vikmarka</span>
  <div class="envelope__body">
    <span class="wordmark">Vikmarka</span>
    <ul class="contact">
      <li><svg width="8" height="8"><use href="#icon-home"/></svg>8640 Brekka</li>
      <li><svg width="8" height="8"><use href="#icon-phone"/></svg>47382950</li>
    </ul>
    <svg class="base-band" viewBox="0 0 685 84" width="685" height="84" preserveAspectRatio="none" aria-hidden="true">
      <path d="M0 56 Q350 70 685 0 V84 H0 Z" fill="url(#band-blue)"/>
    </svg>
    <p class="org-number">Organisation Number 983 517 608</p>
  </div>
</section>

</body>
</html>
```